Name of Business: KUR Advisory. It is a consulting and advisory business providing Investment and f

I am looking for a letterhead (preferably in word) design for a new business that portarys the attributes of professionalism, honesty, integrity and impartiality. I operate in a Regional area called Seabrook which is located about 90min drive from Melbourne CBD on the Victorian coast.

I have an open mind on design and colour: like all things creative it will either hit the spot or not.

Hi - Thank you all for your disigns. We are currently travelling in Australia and can't always get an internet coonnections. We are reviewing all designs and will try and get back to each of your over the next few days. Dennis Walbrook

```html
<!DOCTYPE html>
<html lang="en">
<head>
<meta charset="utf-8">
<title>Seabrook Financial Services — Letterhead</title>
<link rel="stylesheet" href="https://fonts.googleapis.com/css2?family=Questrial&family=Open+Sans:wght@400;700&display=swap">
<style>
  :root {
    --ink: #111111;
    --teal: #1a95b0;
    --teal-light: #b6dde7;
    --paper: #ffffff;
    --page-edge: #e4e4e4;
    --backdrop: #ffffff;
  }
  * { margin: 0; padding: 0; box-sizing: border-box; }
  html, body { width: 1200px; height: 1000px; overflow: hidden; background: var(--backdrop); }
  .canvas { position: relative; width: 1200px; height: 1000px; }

  .letterhead {
    position: absolute; left: 351px; top: 150px; width: 497px; height: 698px;
    background: var(--paper); border: 1px solid var(--page-edge); overflow: hidden;
  }

  .brand {
    position: absolute; left: 12px; top: 30px; display: inline-block;
    color: var(--ink); font-family: "Questrial", sans-serif; font-weight: 400;
  }
  .brand__name { display: block; font-size: 34px; line-height: 1; letter-spacing: 4px; margin-right: -4px; }
  .brand__tagline { display: block; font-size: 12px; line-height: 1; margin-top: 0; text-align: right; }

  .footer { position: absolute; left: 0; right: 0; bottom: 0; height: 46px; font-family: "Open Sans", sans-serif; }
  .footer__mark { position: absolute; left: 27px; top: 1px; width: 40px; height: 40px; border-radius: 50%; background: var(--teal); }
  .footer__band {
    position: absolute; left: 84px; right: 0; height: 11px;
    display: flex; align-items: center; justify-content: space-between;
    padding: 0 20px 0 3px; font-size: 5px; white-space: nowrap;
  }
  .footer__band--web { top: 20px; background: var(--teal-light); color: var(--teal); }
  .footer__band--contact { top: 31px; background: var(--teal); color: #ffffff; padding-right: 14px; }
  .footer__company { font-size: 9px; font-weight: 700; color: var(--teal); letter-spacing: 0.3px; }
  .footer__rule { position: absolute; left: 0; right: 0; bottom: 0; height: 2px; background: var(--ink); }
</style>
</head>
<body>
<div class="canvas">
  <section class="letterhead">
    <header class="brand">
      <span class="brand__name">SEABROOK</span>
      <span class="brand__tagline">Financial Services</span>
    </header>

    <footer class="footer">
      <span class="footer__mark"></span>
      <div class="footer__band footer__band--web">
        <span>&bull; w: www.seabrookfs.com</span>
        <span class="footer__company">Seabrook</span>
      </div>
      <div class="footer__band footer__band--contact">
        <span>&bull; e: info@seabrookfs.com</span>
        <span>&bull; a: Lorem ipsum dolor sit amet, Harbour Road - Seabrook Bay, Coastline &bull; t | 01234 5678</span>
      </div>
      <div class="footer__rule"></div>
    </footer>
  </section>
</div>
</body>
</html>
```